Business Carss for Harborlight Church

Need a progressive looking/modern business card design for my church

Target Market(s)

Families and young adults

Industry/Entity Type

Religious

Contact Information for Business Card

4728 Willow Crest Rd.
Frankfort Ky
502-318-4472

Rev. Tommy Fenwick
Slogan: Honor God and Make Discies

Font styles to use
Serif
Sans Serif
Decorative
Script

Colors
0555a3
3176b5

Requirements
Should not have
• Should not have a template look
• A unique out of the box look

```html
<!DOCTYPE html>
<html lang="en">
<head>
<meta charset="utf-8">
<title>Harborlight Church – Business Card</title>
<link rel="stylesheet" href="https://fonts.googleapis.com/css2?family=Bebas+Neue&family=Open+Sans:wght@400&display=swap">
<style>
  :root {
    --page: #e6e8ec;
    --card: #2b2b2c;
    --card-fold: #232324;
    --band-deep: #2552a0;
    --band-light: #2e78b9;
    --rule: #ffffff;
    --ink: #ffffff;
  }
  * { margin: 0; padding: 0; box-sizing: border-box; }
  html, body { width: 1200px; height: 1200px; overflow: hidden; background: var(--page); }
  .canvas { position: relative; width: 1200px; height: 1200px; }

  .card {
    position: absolute; left: 162px; width: 876px; height: 526px;
    background: var(--card); overflow: hidden;
  }
  .card--front { top: 26px; }
  .card--back { top: 608px; }

  .fold {
    position: absolute; top: 0; bottom: 0; width: 76px;
    background: var(--card-fold);
  }
  .card--front .fold { left: 0; box-shadow: 6px 0 10px rgba(0,0,0,.35); }
  .card--back .fold { right: 0; box-shadow: -6px 0 10px rgba(0,0,0,.35); }

  .name, .slogan {
    position: absolute; font-family: "Bebas Neue", sans-serif;
    color: var(--ink); line-height: 1; letter-spacing: .5px;
  }
  .name { top: 94px; font-size: 44px; }
  .slogan { top: 210px; font-size: 52px; }
  .card--front .name { right: 96px; }
  .card--front .slogan { left: 133px; }
  .card--back .name { left: 109px; }
  .card--back .slogan { right: 140px; }

  .bands { position: absolute; top: 268px; height: 107px; }
  .bands--main { left: 0; right: 0; }
  .card--front .bands--main { left: 76px; }
  .card--back .bands--main { right: 76px; }
  .bands--fold { top: 278px; width: 76px; z-index: 1; }
  .card--front .bands--fold { left: 0; }
  .card--back .bands--fold { right: 0; }

  .rule { height: 10px; background: var(--rule); }
  .band { height: 43px; display: flex; align-items: center; }
  .band--address { height: 44px; background: var(--band-deep); }
  .band--phone { background: var(--band-light); }

  .bands--main .band {
    font-family: "Open Sans", sans-serif; font-size: 22px; color: var(--ink);
  }
  .card--front .bands--main .band { padding-left: 58px; }
  .card--back .bands--main .band { justify-content: flex-end; padding-right: 64px; }

  .bands--fold .band { justify-content: center; }
  .card--front .bands--fold .band { justify-content: flex-end; padding-right: 4px; }
  .card--back .bands--fold .band { justify-content: flex-start; padding-left: 4px; }
  .icon { width: 16px; height: 16px; fill: var(--ink); }
</style>
</head>
<body>
<div class="canvas">

  <section class="card card--front">
    <div class="fold"></div>
    <p class="name">Tommy Fenwick</p>
    <h1 class="slogan">Honor God and Make Discies</h1>
    <div class="bands bands--fold">
      <div class="rule"></div>
      <div class="band band--address">
        <svg class="icon" viewBox="0 0 16 16"><path d="M8 1a5 5 0 0 0-5 5c0 3.6 5 9 5 9s5-5.4 5-9a5 5 0 0 0-5-5zm0 7a2 2 0 1 1 0-4 2 2 0 0 1 0 4z"/></svg>
      </div>
      <div class="band band--phone">
        <svg class="icon" viewBox="0 0 16 16"><path d="M2 5c1-2 3-3 6-3s5 1 6 3l-2 2-2-1V4.5H6V6L4 7 2 5zm2 3h8l1 6H3l1-6zm4 1.5a2 2 0 1 0 0 4 2 2 0 0 0 0-4z"/></svg>
      </div>
      <div class="rule"></div>
    </div>
    <div class="bands bands--main">
      <div class="rule"></div>
      <div class="band band--address">4728 Willow Crest Rd. Frankfort Ky</div>
      <div class="band band--phone">502-318-4472</div>
      <div class="rule"></div>
    </div>
  </section>

  <section class="card card--back">
    <div class="fold"></div>
    <p class="name">Tommy Fenwick</p>
    <h2 class="slogan">Honor God and Make Discies</h2>
    <div class="bands bands--fold">
      <div class="rule"></div>
      <div class="band band--address">
        <svg class="icon" viewBox="0 0 16 16"><path d="M8 1a5 5 0 0 0-5 5c0 3.6 5 9 5 9s5-5.4 5-9a5 5 0 0 0-5-5zm0 7a2 2 0 1 1 0-4 2 2 0 0 1 0 4z"/></svg>
      </div>
      <div class="band band--phone">
        <svg class="icon" viewBox="0 0 16 16"><path d="M2 5c1-2 3-3 6-3s5 1 6 3l-2 2-2-1V4.5H6V6L4 7 2 5zm2 3h8l1 6H3l1-6zm4 1.5a2 2 0 1 0 0 4 2 2 0 0 0 0-4z"/></svg>
      </div>
      <div class="rule"></div>
    </div>
    <div class="bands bands--main">
      <div class="rule"></div>
      <div class="band band--address">4728 Willow Crest Rd. Frankfort Ky</div>
      <div class="band band--phone">502-318-4472</div>
      <div class="rule"></div>
    </div>
  </section>

</div>
</body>
</html>
```